MallPoint Brochure/Booklet Design

I am seeking a luxury finish booklet with the attached content. The same pictures can be used or different ones. It needs to be classy, but EDGY

This new company targets the owners of shopping centres and provides a number of services including marketing/community involvement/digital technology/social media etc. I'd love to see the use of our logo colours and a way to make this really pop!

I'm looking to develop a relationship with a designer that we can work on many more projects with.

I'm not interested in seeing any SAMPLES, only designs that use the brief (our content, logo, colours and font).
Updates

Please do not submit SAMPLES of your other work, we are only interested in seeing designs that work to our brief (content, logo, colour and font)

Reason: There has not been any designs submitted that are of a high enough standard. I'd like to see more use of the colours as backgrounds rather than plain white and some more interesting ideas. Please do not submit samples of your other works.

for brochure inspiration check out the following links... i think bright/classy

Target Market(s)

corporate but with a wow, not standard - this is something millionaires and billionaires will be presented with and they will only look at it for 5 mins so it needs to grab them!

http://www.brelvanto.example/blog/handpicked-printed-brochures/

http://quorvelstudio.example/articles/30-best-brochure-designs-for-your-inspiration/

http://www.tamsifolio.example/2012/04/26/40-unique-and-beautiful-examples-of-brochure-design/

Industry/Entity Type

Shopping

Font styles to use
Other font styles liked:
• ubuntu

Requirements
Must have
• Must have the content supplied included and our logo used
Must use UBUNTU font
Should not have
• Should not be a sample, must abide by the brief

```html
<!DOCTYPE html>
<html lang="en">
<head>
<meta charset="utf-8">
<title>MallPoint Booklet – Team &amp; Presentation</title>
<link rel="stylesheet" href="https://fonts.googleapis.com/css2?family=Ubuntu:wght@300;400;500;700&display=swap">
<style>
  :root {
    --blue: #1667b7;
    --red: #e01f26;
    --green: #1ea34a;
    --yellow: #f7c51c;
    --ink: #5e5e5e;
    --muted: #9a9a9a;
    --numeral: #d9d9d9;
    --rule: #d8d8d8;
    --paper: #f3f3f3;
  }
  * { box-sizing: border-box; margin: 0; padding: 0; }
  html, body { width: 1200px; height: 800px; overflow: hidden; }
  body {
    font-family: "Ubuntu", sans-serif;
    color: var(--ink);
    background: var(--paper);
  }
  .spread {
    position: relative;
    width: 1200px;
    height: 800px;
    overflow: hidden;
    background:
      linear-gradient(90deg, rgba(0,0,0,0) 46%, rgba(0,0,0,0.05) 50%, rgba(0,0,0,0) 54%),
      radial-gradient(ellipse at 25% 45%, #ffffff 0%, #f1f1f1 70%, #e9e9e9 100%),
      var(--paper);
  }
  .page { position: absolute; top: 0; width: 600px; height: 764px; }
  .page--left { left: 0; }
  .page--right { left: 600px; }

  /* page header */
  .brand-mark { position: absolute; top: 18px; display: flex; flex-direction: column; align-items: center; gap: 5px; }
  .brand-mark__square { width: 30px; height: 30px; background: var(--green); }
  .brand-mark__name { font-size: 11px; font-weight: 500; color: var(--blue); }
  .page--left .brand-mark { left: 16px; }
  .page--right .brand-mark { right: 16px; }

  .page-number {
    position: absolute; top: 24px;
    font-size: 64px; font-weight: 300; line-height: 1; color: var(--numeral);
    letter-spacing: -2px;
  }
  .page-rule { position: absolute; top: 0; width: 2px; height: 82px; background: #8cc63f; }
  .page-label { position: absolute; font-size: 16px; font-weight: 300; color: #c4c4c4; line-height: 19px; }
  .page--left .page-number { left: 76px; }
  .page--left .page-rule { left: 138px; }
  .page--left .page-label { left: 146px; top: 47px; }
  .page--right .page-number { left: 454px; }
  .page--right .page-rule { left: 443px; }
  .page--right .page-label { right: 164px; top: 65px; }

  /* content */
  .section-title {
    position: absolute; left: 28px; top: 190px;
    font-size: 28px; font-weight: 500; color: var(--red); letter-spacing: 0.5px;
  }
  .intro {
    position: absolute; left: 31px; top: 229px; width: 460px;
    font-size: 14px; line-height: 20px; color: var(--muted);
  }
  .list-title {
    position: absolute; left: 31px;
    font-size: 16px; font-weight: 500; color: var(--green); letter-spacing: 0.4px;
  }
  .service-list { position: absolute; left: 28px; width: 275px; list-style: none; }
  .service-list li {
    display: flex; padding: 8px 0 9px 6px;
    border-bottom: 1px solid var(--rule);
    font-size: 14px; line-height: 20px;
  }
  .service-list li:last-child { border-bottom: none; }
  .service-list .num { width: 34px; flex: none; color: var(--green); font-weight: 500; }
  .page--right .section-title,
  .page--right .intro,
  .page--right .list-title,
  .page--right .service-list { left: 24px; }
  .page--right .intro { left: 24px; }
  .page--right .service-list { width: 276px; }

  .photo {
    position: absolute; top: 331px; height: 204px;
    border-top: 3px solid var(--blue); border-bottom: 3px solid var(--blue);
  }
  .photo--team { left: 330px; width: 271px; background: linear-gradient(135deg, #dfe6ee 0%, #8a8f96 45%, #2f3338 100%); }
  .photo--checklist { left: 364px; width: 236px; background: linear-gradient(135deg, #ffffff 0%, #c9d6ee 50%, #3d5fb0 100%); }

  .experience-band {
    position: absolute; left: 0; top: 572px; width: 574px; height: 42px;
    background: var(--blue); color: #fff;
    font-size: 18px; font-weight: 500; line-height: 42px; padding-left: 15px;
    letter-spacing: 0.2px;
  }
  .experience-band strong { color: var(--yellow); font-weight: 700; }
  .band-stripes { position: absolute; left: 580px; top: 572px; display: flex; gap: 4px; }
  .band-stripes span { width: 8px; height: 42px; }
  .band-stripes .r { background: var(--red); }
  .band-stripes .g { background: var(--green); }

  /* footer */
  .footer { position: absolute; left: 0; bottom: 0; width: 1200px; height: 36px; display: flex; gap: 3px; }
  .footer__blue { width: 800px; background: var(--blue); color: #fff; font-size: 20px; font-weight: 500; line-height: 36px; padding-left: 16px; }
  .footer__red { width: 197px; background: var(--red); }
  .footer__green { flex: 1; background: var(--green); }
</style>
</head>
<body>
<main class="spread">

  <section class="page page--left">
    <div class="brand-mark"><span class="brand-mark__square"></span><span class="brand-mark__name">MallPoint</span></div>
    <div class="page-number">01</div>
    <div class="page-rule"></div>
    <div class="page-label">Your<br>Centre Team</div>

    <h1 class="section-title">Your Centre Team</h1>
    <p class="intro">Hand-picked specialised team of experienced and Highly Qualified Professionals</p>

    <h2 class="list-title" style="top:296px">ALL-ENCOMPASSING SERVICE</h2>
    <ol class="service-list" style="top:323px">
      <li><span class="num">01</span><span>Graphic Design Artists</span></li>
      <li><span class="num">02</span><span>IT integratation / Support technicians</span></li>
      <li><span class="num">03</span><span>Marketing Gurus</span></li>
      <li><span class="num">04</span><span>Retail Consultancy experts</span></li>
      <li><span class="num">05</span><span>Your own ‘on the ground’ person ideally sourced from your catchment</span></li>
    </ol>

    <div class="photo photo--team" role="img" aria-label="Photo of a business team joining hands in a circle"></div>

    <p class="experience-band">Combined experience of over <strong>100 years</strong> in the retail sector</p>
    <div class="band-stripes"><span class="r"></span><span class="g"></span></div>
  </section>

  <section class="page page--right">
    <div class="page-label">Presentation</div>
    <div class="page-rule"></div>
    <div class="page-number">02</div>
    <div class="brand-mark"><span class="brand-mark__square"></span><span class="brand-mark__name">MallPoint</span></div>

    <h1 class="section-title">Presentation</h1>
    <p class="intro">Please read below comments for persentation facilities and&nbsp; Your centre known in the community</p>

    <h2 class="list-title" style="top:296px">Facilities</h2>
    <ol class="service-list" style="top:323px">
      <li><span class="num">01</span><span>Layout and usability optimisation</span></li>
      <li><span class="num">02</span><span>Appearance and presentation</span></li>
      <li><span class="num">03</span><span>Cleanliness / OH &amp; S</span></li>
    </ol>

    <h2 class="list-title" style="top:473px">Your centre known in the community</h2>
    <ol class="service-list" style="top:500px">
      <li><span class="num">01</span><span>Branding – recognisable / memorable</span></li>
      <li><span class="num">02</span><span>Better shopping experience</span></li>
      <li><span class="num">03</span><span>Improved image – giving back / rewarding</span></li>
    </ol>

    <div class="photo photo--checklist" role="img" aria-label="Image of a rating checklist with red ticks beside Excellent and Good"></div>
  </section>

  <footer class="footer">
    <div class="footer__blue">MallPoint</div>
    <div class="footer__red"></div>
    <div class="footer__green"></div>
  </footer>

</main>
</body>
</html>
```